Extend Medium Rectangle into Halfpage and Billboard Ad Format

We have a few variations of our Medium Rectangle (300x250) that we use to build scalable online ads for local advertisers based on their images and logos which in most of the cases are very basic but still should deliver decent results in terms of overall banner look.

Based on those variations we would like to have each a Halfpage and Billboard variation to it that resembles the "look & feel" to feel like "out of one hand" and allows the local advertiser to recognize his ad across all formats.

Core of the Medium Rectangle is a carousel ad to swipe through the images and "more information" for the click-out to the landingpage. That might be great to replicate on the other banner formats but also could be done differently.

Attached the examples we have for one local customer to build ads from. Very limited but realistic.

```html
<!DOCTYPE html>
<html lang="de">
<head>
<meta charset="utf-8">
<title>Gasthof Sonne – Halfpage</title>
<link rel="stylesheet" href="https://fonts.googleapis.com/css2?family=Open+Sans:wght@400;600&display=swap">
<style>
  :root {
    --red-deep: #9e0a10;
    --red: #c0121a;
    --red-bright: #cf1a22;
    --white: #ffffff;
    --yellow: #f6c21a;
    --yellow-edge: #d9a30c;
    --ink: #2a1a0e;
    --photo-warm: #c98a52;
    --photo-red: #8e1a1c;
    --photo-cream: #eed9b6;
  }
  html, body {
    margin: 0;
    padding: 0;
    width: 1200px;
    height: 2400px;
    overflow: hidden;
    background: var(--white);
  }
  .ad {
    position: relative;
    width: 1200px;
    height: 2400px;
    overflow: hidden;
    background: linear-gradient(180deg, var(--red-deep) 0%, var(--red) 55%, var(--red-bright) 100%);
    font-family: "Open Sans", Arial, sans-serif;
  }
  .hero {
    position: absolute;
    inset: 0 0 auto 0;
    width: 1200px;
    height: 1300px;
  }
  .nav {
    position: absolute;
    top: 1310px;
    width: 90px;
    height: 140px;
  }
  .nav--prev { left: 50px; }
  .nav--next { right: 50px; }
  .brand {
    position: absolute;
    top: 1480px;
    left: 0;
    width: 1200px;
    text-align: center;
    color: var(--white);
    font-weight: 400;
    font-size: 190px;
    line-height: 1;
    letter-spacing: 6px;
  }
  .headline {
    position: absolute;
    top: 1780px;
    left: 0;
    width: 1200px;
    margin: 0;
    text-align: center;
    color: var(--white);
    font-weight: 600;
    font-size: 80px;
    line-height: 116px;
  }
  .cta {
    position: absolute;
    left: 312px;
    top: 2192px;
    width: 576px;
    height: 128px;
    box-sizing: border-box;
    border-radius: 12px;
    background: var(--yellow);
    border: 4px solid var(--yellow-edge);
    color: var(--ink);
    font-size: 68px;
    font-weight: 400;
    line-height: 120px;
    text-align: center;
  }
</style>
</head>
<body>
  <div class="ad">
    <svg class="hero" viewBox="0 0 1200 1300" xmlns="http://www.w3.org/2000/svg">
      <defs>
        <linearGradient id="photoTone" x1="0" y1="0" x2="1" y2="1">
          <stop offset="0" stop-color="var(--photo-cream)"/>
          <stop offset="0.35" stop-color="var(--photo-warm)"/>
          <stop offset="0.7" stop-color="var(--photo-red)"/>
          <stop offset="1" stop-color="#3a1c12"/>
        </linearGradient>
      </defs>
      <path class="hero__swoosh" d="M0 960 C380 1090 820 1200 1200 1150 L1200 1230 C820 1290 360 1190 0 1060 Z" fill="var(--white)"/>
      <path class="hero__photo" role="img" aria-label="Foto des Gastraums mit gedeckten Tischen, roten Stühlen und Servietten"
            d="M0 0 H1200 V1150 C820 1200 380 1090 0 960 Z" fill="url(#photoTone)"/>
    </svg>

    <svg class="nav nav--prev" viewBox="0 0 90 140" aria-label="Vorheriges Bild">
      <polyline points="70,15 20,70 70,125" fill="none" stroke="var(--white)" stroke-width="12" stroke-linecap="round" stroke-linejoin="round"/>
    </svg>
    <svg class="nav nav--next" viewBox="0 0 90 140" aria-label="Nächstes Bild">
      <polyline points="20,15 70,70 20,125" fill="none" stroke="var(--white)" stroke-width="12" stroke-linecap="round" stroke-linejoin="round"/>
    </svg>

    <div class="brand">SONNE</div>

    <p class="headline">Neueröffnung Gasthof<br>Sonne in Tannbach</p>

    <div class="cta">Mehr erfahren</div>
  </div>
</body>
</html>
```